I want a business card that is going to show a creative spark but without limiting me to an industry. Something edgy but that wont go out of date. I want it state My business name Serafina Loire, profession - Professional Makeup Artist contact number and email

My service is to provide makeup services from bridal, fashion, photography, film, TV and so on. It is creative and different so i want that to be reflected.

I would like the card double sided.
Updates

 I would LOVE a background on my card something like this image... i can supply an image to be formed like this

Please use the image uploaded

Can we try using the image provided on one side of the card and then writing and details on the other side

Target Market(s)

I am targeting a wide range of people from Creative directors to the individual eg. bride

Industry/Entity Type

Business

Requirements
Must have
• Name: Delphine Hartwell
contact numbe 0417853120
email address:info@serafinaloire.com
website: www.serafinaloire.com
One of the images attached

professional makeup artist / hair stylist

I want it to show creativity
Nice to have
• logo, Double-sided card
Should not have
• the design should not use tradional style. Or images that are not my own

```html
<!DOCTYPE html>
<html lang="en">
<head>
<meta charset="utf-8">
<title>Serafina Loire – Business Card Options</title>
<link rel="stylesheet" href="https://fonts.googleapis.com/css2?family=Poiret+One&family=Cormorant+Garamond:ital,wght@1,500&family=Caveat:wght@500&family=Encode+Sans+Condensed:wght@600&family=Sorts+Mill+Goudy&display=swap">
<style>
  :root {
    --paper: #ffffff;
    --card-edge: #111111;
    --ink-night: #1d1b46;
    --ink-deep: #252a7e;
    --ink-royal: #2f3aa3;
    --ink-periwinkle: #5560b8;
    --name-silver: #c9ccd8;
    --label-lavender: #cfd0f2;
    --card-w: 459px;
    --card-h: 748px;
  }
  * { margin: 0; padding: 0; box-sizing: border-box; }
  html, body {
    width: 1200px;
    height: 2942px;
    overflow: hidden;
    background: var(--paper);
  }
  .sheet { position: relative; width: 1200px; height: 2942px; }

  .card {
    position: absolute;
    width: var(--card-w);
    height: var(--card-h);
    border: 3px solid var(--card-edge);
    overflow: hidden;
  }
  .card--front { left: 31px; }
  .card--back  { left: 570px; }
  .row-1 { top: 169px; }
  .row-2 { top: 1074px; }
  .row-3 { top: 2018px; }

  .card__artwork {
    position: absolute;
    inset: 0;
    background:
      radial-gradient(ellipse 30% 45% at 50% 60%, var(--ink-royal) 0%, transparent 70%),
      radial-gradient(ellipse 40% 25% at 15% 20%, var(--ink-periwinkle) 0%, transparent 70%),
      radial-gradient(ellipse 35% 30% at 85% 85%, var(--ink-periwinkle) 0%, transparent 70%),
      radial-gradient(ellipse 45% 35% at 80% 25%, var(--ink-deep) 0%, transparent 75%),
      linear-gradient(160deg, var(--ink-deep) 0%, var(--ink-night) 45%, var(--ink-royal) 100%);
  }
  .card--back .card__artwork {
    background:
      radial-gradient(ellipse 18% 60% at 50% 55%, var(--ink-royal) 0%, transparent 70%),
      radial-gradient(ellipse 35% 25% at 90% 20%, var(--ink-periwinkle) 0%, transparent 70%),
      radial-gradient(ellipse 30% 30% at 10% 85%, var(--ink-deep) 0%, transparent 70%),
      linear-gradient(200deg, var(--ink-deep) 0%, var(--ink-night) 50%, var(--ink-royal) 100%);
  }

  .text { position: absolute; line-height: 1; white-space: nowrap; }

  /* Profession label, shared by every front */
  .profession {
    font-family: "Encode Sans Condensed", "Arial Narrow", sans-serif;
    font-weight: 600;
    color: var(--label-lavender);
    letter-spacing: -0.5px;
  }
  .profession--title { font-size: 44px; top: 618px; }
  .profession--role  { font-size: 38px; top: 666px; }

  /* Contact block on backs */
  .contact { left: 0; width: 100%; text-align: center; color: var(--label-lavender); }
  .contact--sans {
    font-family: "Encode Sans Condensed", "Arial Narrow", sans-serif;
    font-weight: 600;
  }
  .contact--serif { font-family: "Sorts Mill Goudy", Georgia, serif; }

  /* Option 1: geometric light */
  .name-geo { font-family: "Poiret One", "Century Gothic", sans-serif; color: var(--name-silver); }
  .name-geo--first { font-size: 66px; top: 216px; left: 106px; }
  .name-geo--last  { font-size: 122px; top: 291px; left: 68px; }
  .row-1 .profession { left: 124px; }
  .row-1 .phone { font-size: 44px; top: 638px; }
  .row-1 .email { font-size: 36px; top: 693px; }

  /* Option 2: outlined italic serif */
  .name-serif {
    font-family: "Cormorant Garamond", Georgia, serif;
    font-style: italic;
    font-weight: 500;
    color: transparent;
    -webkit-text-stroke: 1.6px var(--name-silver);
  }
  .name-serif--first { font-size: 92px; top: 155px; left: 40px; }
  .name-serif--last  { font-size: 112px; top: 250px; left: 66px; }
  .row-2 .profession { left: 120px; }
  .row-2 .phone { font-size: 40px; top: 650px; letter-spacing: 3px; }
  .row-2 .email { font-size: 30px; top: 698px; }

  /* Option 3: loose hand */
  .name-hand { font-family: "Caveat", "Comic Sans MS", cursive; font-weight: 500; color: var(--name-silver); }
  .name-hand--first { font-size: 52px; top: 222px; left: 126px; }
  .name-hand--last  { font-size: 180px; top: 250px; left: 30px; transform: rotate(-4deg); transform-origin: left bottom; }
  .row-3 .profession { left: 111px; }
  .row-3 .phone { font-size: 44px; top: 640px; }
  .row-3 .email { font-size: 36px; top: 690px; }
</style>
</head>
<body>
<main class="sheet">

  <!-- Option 1 -->
  <section class="card card--front row-1">
    <div class="card__artwork" role="img" aria-label="Client's own close-up photograph of a flower in deep indigo and royal blue tones"></div>
    <p class="text name-geo name-geo--first">Serafina</p>
    <p class="text name-geo name-geo--last">Loire</p>
    <p class="text profession profession--title">Professional</p>
    <p class="text profession profession--role">Makeup Artist</p>
  </section>
  <section class="card card--back row-1">
    <div class="card__artwork" role="img" aria-label="Client's own close-up photograph of flower petals in indigo and blue tones"></div>
    <p class="text contact contact--sans phone">0417853120</p>
    <p class="text contact contact--sans email">serafinaloire@mail.com.au</p>
  </section>

  <!-- Option 2 -->
  <section class="card card--front row-2">
    <div class="card__artwork" role="img" aria-label="Client's own close-up photograph of a flower in deep indigo and royal blue tones"></div>
    <p class="text name-serif name-serif--first">Serafina</p>
    <p class="text name-serif name-serif--last">Loire</p>
    <p class="text profession profession--title">Professional</p>
    <p class="text profession profession--role">Makeup Artist</p>
  </section>
  <section class="card card--back row-2">
    <div class="card__artwork" role="img" aria-label="Client's own close-up photograph of flower petals in indigo and blue tones"></div>
    <p class="text contact contact--serif phone">0417853120</p>
    <p class="text contact contact--serif email">serafinaloire@mail.com.au</p>
  </section>

  <!-- Option 3 -->
  <section class="card card--front row-3">
    <div class="card__artwork" role="img" aria-label="Client's own close-up photograph of a flower in deep indigo and royal blue tones"></div>
    <p class="text name-hand name-hand--first">Serafina</p>
    <p class="text name-hand name-hand--last">Loire</p>
    <p class="text profession profession--title">Professional</p>
    <p class="text profession profession--role">Makeup Artist</p>
  </section>
  <section class="card card--back row-3">
    <div class="card__artwork" role="img" aria-label="Client's own close-up photograph of flower petals in indigo and blue tones"></div>
    <p class="text contact contact--sans phone">0417853120</p>
    <p class="text contact contact--sans email">serafinaloire@mail.com.au</p>
  </section>

</main>
</body>
</html>
```